Travel Blogger Business Card for roamquill.net

I need a two-sided business card for a travel blogging website. The card should be both professional and fun at the same time. This is for the website www.roamquill.net

I don't necessarily think that the current logo on the website needs to be used on the business card but it can be. I am very flexible with ideas

Target Market(s)

Travel agencies that will be met at a conference.

Industry/Entity Type

Travel

Contact Information for Business Card

Company Name: Roam Quill.net
Name: Bertrand Olesky
Voice: +1-(345)-402-7731
Address: Coral Reach Shore, Grand Cayman, Cayman Islands
Email: ceo@roamquill.net

Colors
0592cd
0355a3
3176b5
33a6d7
85cae6
85acd3

Requirements
Must have
• Website address and name should be bigger than address, phone number, and email.

```html
<!DOCTYPE html>
<html lang="en">
<head>
<meta charset="utf-8">
<title>Roam Quill – Business Card</title>
<link rel="stylesheet" href="https://fonts.googleapis.com/css2?family=Arimo:wght@400;700&display=swap">
<style>
  :root {
    --stage: #3b3532;
    --card: #161718;
    --card-edge: #222426;
    --brand-blue: #33a6d7;
    --text-light: #e9ecef;
    --text-muted: #c4c8cc;
    --mark-grey: #9a9d9f;
    --url-grey: #8b8f93;
  }
  * { margin: 0; padding: 0; box-sizing: border-box; }
  html, body { width: 1200px; height: 864px; overflow: hidden; }
  body {
    background: var(--stage);
    font-family: "Arimo", Arial, sans-serif;
    display: flex;
    align-items: center;
    justify-content: center;
    gap: 40px;
  }
  .card {
    position: relative;
    width: 520px;
    height: 298px;
    background: var(--card);
    border: 1px solid var(--card-edge);
    box-shadow: 0 14px 30px rgba(0,0,0,.45);
  }

  /* Back side */
  .card-back .back-mark {
    position: absolute;
    left: 0; right: 0; top: 88px;
    display: flex;
    align-items: center;
    justify-content: center;
    gap: 14px;
  }
  .back-mark .mark-dot {
    width: 34px; height: 34px; border-radius: 50%;
    background: var(--mark-grey);
  }
  .back-mark .mark-name {
    font-weight: 700;
    font-size: 40px;
    color: var(--mark-grey);
    letter-spacing: 1px;
  }
  .card-back .back-url {
    position: absolute;
    left: 0; right: 0; top: 196px;
    text-align: center;
    font-size: 12px;
    letter-spacing: 3px;
    color: var(--url-grey);
  }

  /* Front side */
  .front-logo {
    position: absolute;
    left: 210px; top: 72px;
    display: flex; align-items: center; gap: 10px;
  }
  .front-logo .logo-dot {
    width: 26px; height: 26px; border-radius: 50%;
    background: var(--text-light);
  }
  .front-logo .logo-name {
    font-weight: 700;
    font-size: 32px;
    color: var(--brand-blue);
    letter-spacing: .5px;
  }
  .identity {
    position: absolute;
    right: 230px; top: 148px;
    text-align: right;
  }
  .identity .person-name {
    font-size: 19px;
    color: var(--brand-blue);
    margin-bottom: 6px;
  }
  .identity .address-line {
    font-size: 13px;
    color: var(--text-muted);
    line-height: 17px;
  }
  .divider {
    position: absolute;
    left: 302px; top: 150px;
    width: 1px; height: 84px;
    background: var(--text-muted);
    opacity: .7;
  }
  .contacts {
    position: absolute;
    left: 316px; top: 166px;
    list-style: none;
  }
  .contacts li {
    display: flex; align-items: center; gap: 8px;
    font-size: 14px;
    color: var(--text-light);
    height: 22px;
  }
  .contacts svg { width: 13px; height: 13px; flex: none; }
</style>
</head>
<body>

  <section class="card card-back" aria-label="Card back">
    <div class="back-mark">
      <span class="mark-dot"></span>
      <span class="mark-name">ROAM QUILL</span>
    </div>
    <p class="back-url">www.roamquill.net</p>
  </section>

  <section class="card card-front" aria-label="Card front">
    <div class="front-logo">
      <span class="logo-dot"></span>
      <span class="logo-name">ROAM QUILL</span>
    </div>

    <div class="identity">
      <p class="person-name">Bertrand Olesky</p>
      <p class="address-line">Coral Reach Shore</p>
      <p class="address-line">Grand Cayman, Cayman Islands</p>
    </div>

    <span class="divider"></span>

    <ul class="contacts">
      <li>
        <svg viewBox="0 0 16 16" aria-hidden="true"><path fill="#33a6d7" d="M3.5 1.5l2.5 0 1 3.5-1.6 1.2a8 8 0 0 0 4.4 4.4L11 9l3.5 1v2.5c0 1-1 2-2 2A11 11 0 0 1 1.5 3.5c0-1 1-2 2-2z"/></svg>
        +1-(345)-402-7731
      </li>
      <li>
        <svg viewBox="0 0 16 16" aria-hidden="true"><rect x="1" y="3" width="14" height="10" rx="1.5" fill="#33a6d7"/><path d="M1.5 4l6.5 5 6.5-5" fill="none" stroke="#161718" stroke-width="1.4"/></svg>
        ceo@roamquill.net
      </li>
      <li>
        <svg viewBox="0 0 16 16" aria-hidden="true"><circle cx="8" cy="8" r="7" fill="#33a6d7"/><path d="M1 8h14M8 1c-3 3.5-3 10.5 0 14M8 1c3 3.5 3 10.5 0 14" fill="none" stroke="#161718" stroke-width="1.1"/></svg>
        www.roamquill.net
      </li>
    </ul>
  </section>

</body>
</html>
```